Corvane Tables business cards

I’d like a business card design that includes my logo, a tag line and my contact info. Black, textured background. My contact info color should match the orange and blue gradients. Tagline under logo: “Wooden Tables and Furniture of the Highest Quality”

Target Market(s)

High end furniture buyers

Contact Information for Business Card

Contact info, logo and tagline

```html
<!DOCTYPE html>
<html lang="en">
<head>
<meta charset="utf-8">
<title>Corvane Tables business cards</title>
<link rel="stylesheet" href="https://fonts.googleapis.com/css2?family=Montserrat:wght@400;500;600;700&family=Oswald:wght@500&display=swap">
<style>
  :root {
    --page-bg: #e4e4e4;
    --card-white: #ffffff;
    --card-white-shade: #f3f3f3;
    --card-black: #0f0f0f;
    --card-black-soft: #1c1c1c;
    --orange: #e8702a;
    --orange-red: #f2613d;
    --orange-light: #fb9645;
    --blue: #2b63b1;
    --blue-light: #4aa3e0;
    --ink: #262626;
    --paper-text: #ffffff;
  }
  * { box-sizing: border-box; margin: 0; padding: 0; }
  html, body { width: 1200px; height: 1200px; overflow: hidden; }
  body {
    background: var(--page-bg);
    font-family: "Montserrat", Arial, sans-serif;
    display: flex;
    flex-direction: column;
    align-items: center;
    justify-content: center;
    gap: 44px;
  }
  .card {
    position: relative;
    width: 900px;
    height: 514px;
    border-radius: 30px;
    overflow: hidden;
    box-shadow: 0 10px 28px rgba(0,0,0,0.22);
  }

  /* Front */
  .card--front {
    background: linear-gradient(180deg, var(--card-white) 0%, var(--card-white-shade) 100%);
  }
  .brand {
    position: absolute;
    display: flex;
    align-items: center;
    gap: 16px;
  }
  .brand__dot {
    width: 34px; height: 34px;
    border-radius: 50%;
    background: var(--orange);
    flex: none;
  }
  .brand__name {
    font-weight: 600;
    white-space: nowrap;
  }
  .card--front .brand { right: 80px; top: 120px; }
  .card--front .brand__name { font-size: 52px; color: var(--blue); }

  .identity {
    position: absolute;
    left: 80px;
    top: 250px;
    border-left: 7px solid var(--orange);
    padding-left: 16px;
  }
  .identity__name {
    font-size: 40px;
    font-weight: 600;
    color: var(--orange);
    letter-spacing: 1px;
    line-height: 1;
  }
  .identity__role {
    font-size: 19px;
    font-weight: 500;
    color: var(--ink);
    letter-spacing: 1px;
    margin-top: 4px;
  }
  .contact {
    position: absolute;
    left: 82px;
    top: 345px;
    list-style: none;
    display: flex;
    flex-direction: column;
    gap: 8px;
  }
  .contact__item {
    display: flex;
    align-items: center;
    gap: 14px;
    font-size: 21px;
    color: var(--ink);
    letter-spacing: 0.5px;
  }
  .contact__icon { width: 24px; height: 24px; flex: none; }

  .band {
    position: absolute;
    bottom: 0;
    height: 16px;
  }
  .band--orange {
    left: 0; width: 58%;
    background: linear-gradient(90deg, var(--orange-red), var(--orange-light) 55%, var(--orange-red));
  }
  .band--blue {
    right: 0; width: 41%;
    background: var(--blue);
  }

  /* Back */
  .card--back {
    background:
      radial-gradient(circle at 35% 30%, rgba(255,255,255,0.05), transparent 55%),
      linear-gradient(135deg, var(--card-black) 0%, var(--card-black-soft) 50%, var(--card-black) 100%);
  }
  .card--back .brand {
    left: 50%; top: 170px;
    transform: translateX(-50%);
  }
  .card--back .brand__dot { width: 44px; height: 44px; }
  .card--back .brand__name { font-size: 70px; color: var(--orange-light); }
  .tagline {
    position: absolute;
    left: 0; right: 0;
    top: 285px;
    text-align: center;
    font-family: "Oswald", "Arial Narrow", sans-serif;
    font-weight: 500;
    font-size: 27px;
    letter-spacing: 1px;
    text-transform: uppercase;
    color: var(--paper-text);
  }
  .card--back .band--accent {
    left: 48%; width: 40%;
    bottom: 60px;
    height: 20px;
    background: linear-gradient(90deg, var(--orange-red), var(--orange-light) 55%, var(--orange-red));
  }
</style>
</head>
<body>
  <section class="card card--front" aria-label="Business card front">
    <div class="brand">
      <span class="brand__dot"></span>
      <span class="brand__name">Corvane Tables</span>
    </div>

    <div class="identity">
      <p class="identity__name">JOHN DOE</p>
      <p class="identity__role">POSITION</p>
    </div>

    <ul class="contact">
      <li class="contact__item">
        <svg class="contact__icon" viewBox="0 0 24 24" aria-hidden="true"><path fill="#e8702a" d="M6.6 10.8a15.1 15.1 0 0 0 6.6 6.6l2.2-2.2a1 1 0 0 1 1-.25 11.4 11.4 0 0 0 3.6.57 1 1 0 0 1 1 1V20a1 1 0 0 1-1 1A17 17 0 0 1 3 4a1 1 0 0 1 1-1h3.5a1 1 0 0 1 1 1c0 1.25.2 2.45.57 3.57a1 1 0 0 1-.25 1z"/></svg>
        <span>(000) 000 0000</span>
      </li>
      <li class="contact__item">
        <svg class="contact__icon" viewBox="0 0 24 24" aria-hidden="true"><rect x="2" y="5" width="20" height="14" rx="1" fill="#e8702a"/><path d="M2.5 5.5 12 13l9.5-7.5" fill="none" stroke="#fff" stroke-width="1.6"/></svg>
        <span>email@youremail.com</span>
      </li>
      <li class="contact__item">
        <svg class="contact__icon" viewBox="0 0 24 24" aria-hidden="true"><circle cx="12" cy="12" r="10" fill="#e8702a"/><g fill="none" stroke="#fff" stroke-width="1.3"><ellipse cx="12" cy="12" rx="4" ry="10"/><path d="M2 12h20M4 7h16M4 17h16"/></g></svg>
        <span>www.yourwebsite.com</span>
      </li>
    </ul>

    <div class="band band--orange"></div>
    <div class="band band--blue"></div>
  </section>

  <section class="card card--back" aria-label="Business card back">
    <div class="brand">
      <span class="brand__dot"></span>
      <span class="brand__name">Corvane Tables</span>
    </div>
    <p class="tagline">Wooden Tables and Furniture of the Highest Quality</p>
    <div class="band band--accent"></div>
  </section>
</body>
</html>
```